International professional tennis coach needs a book cover design

This is my 2nd published book, the first one was a #1 on the best seller. I'm looking for a world class book cover design for this new book. The name of my first book was 5 Baseline Habits to Unlock Your Rally Rhythm, located on Brimlow.com

The title of the new book:

Title: The Craft of Steady Rallies
Subtitle: Building a Tactical Margin by Way of Opponent Insight

I'm uploading our new CRAFT OF STEADY logo that I'd like for you to use as the centerpiece of the book design along with a 21st century design feel that incorporates what the book topic is below::

--> This book is about building competitive intelligence by using tennis data analytics to develop and expand a player's strategic advantage for match play. <--

The colors we would like to use are Blue, Yellow, and Green. These shades of these colors should be bold! (You will see the bold color examples of blues, yellows, and greens that I'm talking about in the logos that are attached here, especially the colors for my Tennis GridRally App logo.

I will upload the Tennis GridRally logo which should go somewhere on the back cover design (small size maybe in the bottom corner).

This book is revolutionary to the standard way of teaching tennis, it is based on a decade of recording and gathering tennis data analytics and then we created on-court practice games to develop better decision making in players for the competitive edge.

My websites are www.elevatedrillzone.com and www.craftofsteadyrallies.com

```html
<!DOCTYPE html>
<html lang="en">
<head>
<meta charset="utf-8">
<title>The Craft of Steady Rallies – Book Cover</title>
<link rel="stylesheet" href="https://fonts.googleapis.com/css2?family=Oswald:wght@200;500;700&family=Montserrat:wght@400&display=swap">
<style>
  :root {
    --page-bg: #e9e9e6;
    --cover-green-light: #3aac72;
    --cover-green: #16a05a;
    --cover-green-dark: #07924d;
    --title-white: #ffffff;
    --title-yellow: #f7bf1e;
    --rule-yellow: #c9c83a;
    --brand-blue: #1f82cf;
  }
  * { margin: 0; padding: 0; box-sizing: border-box; }
  html, body {
    width: 1200px;
    height: 800px;
    overflow: hidden;
    background: var(--page-bg);
  }
  .stage {
    width: 1200px;
    height: 800px;
    display: flex;
    align-items: center;
    justify-content: center;
  }
  .book-cover {
    position: relative;
    width: 500px;
    height: 750px;
    background: linear-gradient(160deg, var(--cover-green-light) 0%, var(--cover-green) 45%, var(--cover-green-dark) 100%);
    color: var(--title-white);
    display: flex;
    flex-direction: column;
    align-items: center;
    padding: 46px 36px 40px;
    box-shadow: 0 6px 24px rgba(0,0,0,0.18);
  }
  .title {
    text-align: center;
    font-family: 'Oswald', sans-serif;
    text-transform: uppercase;
    line-height: 0.88;
  }
  .title-lead {
    display: block;
    font-weight: 200;
    font-size: 84px;
    letter-spacing: -1px;
  }
  .title-accent {
    display: block;
    font-weight: 700;
    font-size: 128px;
    letter-spacing: -2px;
    color: var(--title-yellow);
  }
  .title-main {
    display: block;
    font-weight: 700;
    font-size: 128px;
    letter-spacing: -2px;
    color: var(--title-white);
  }
  .brand-mark {
    margin-top: 40px;
    display: flex;
    align-items: center;
    gap: 14px;
  }
  .brand-mark-dot {
    width: 30px;
    height: 30px;
    border-radius: 50%;
    background: var(--brand-blue);
  }
  .brand-mark-name {
    font-family: 'Oswald', sans-serif;
    font-weight: 500;
    font-size: 34px;
    letter-spacing: 1px;
    color: var(--title-yellow);
  }
  .subtitle {
    margin-top: 44px;
    width: 100%;
    padding: 12px 0;
    border-top: 1px solid var(--rule-yellow);
    border-bottom: 1px solid var(--rule-yellow);
    font-family: 'Montserrat', sans-serif;
    font-weight: 400;
    font-size: 21px;
    line-height: 1.3;
    letter-spacing: 1px;
    text-align: center;
  }
  .authors {
    margin-top: auto;
    font-family: 'Oswald', sans-serif;
    font-weight: 500;
    font-size: 36px;
    letter-spacing: 0.5px;
    text-transform: uppercase;
    text-align: center;
  }
</style>
</head>
<body>
  <main class="stage">
    <section class="book-cover">
      <h1 class="title">
        <span class="title-lead">The Craft of</span>
        <span class="title-accent">Steady</span>
        <span class="title-main">Rallies</span>
      </h1>
      <div class="brand-mark">
        <span class="brand-mark-dot"></span>
        <span class="brand-mark-name">CRAFT OF STEADY</span>
      </div>
      <p class="subtitle">Building a Tactical Margin<br>by Way of Opponent Insight</p>
      <p class="authors">Marlow Kestrel &amp; Dane Porter</p>
    </section>
  </main>
</body>
</html>
```